Real Estate "For Sale" Sign for construction company

We need a sign that we can use to hang on a post and place on the road when we sell a property. The sign will be simple and will need to mainly feature our logo (files attached), as well as the words "For Sale", and then our phone number "(555) 617 3489". The sign will hang on a post that'll look something like the attached picture.

Target Market(s)

Home buyers

Industry/Entity Type

Real Estate

Font styles to use
Serif
Sans Serif

Colors
0054AA
0677BA
7BADD7
CADEEF
E8F1F8
0094D4
00A9DD
6FCCEA
C7EBF8
E9F6FB

Requirements
Must have
• For Sale & our phone number

```html
<!DOCTYPE html>
<html lang="en">
<head>
<meta charset="utf-8">
<title>For Sale Sign – Laurel Creek Homes</title>
<link href="https://fonts.googleapis.com/css2?family=Rubik:wght@400;700;800&display=swap" rel="stylesheet">
<style>
  :root{
    --royal:#0b4ce3;
    --cyan:#0ff4f6;
    --navy:#0d1858;
    --sky:#7cc6f4;
    --ice:#cdeef9;
    --mist:#ebf6fb;
    --brand-text:#3a8be8;
    --white:#ffffff;
  }
  html,body{margin:0;padding:0;overflow:hidden;background:var(--white);}
  .canvas{position:relative;width:1200px;height:1200px;overflow:hidden;background:var(--white);}
  .sign{
    position:absolute;left:190px;top:50px;
    width:892px;height:1198px;
    transform:scale(0.918);transform-origin:top left;
    background:var(--white);
    outline:1.5px solid #222;
    font-family:"Rubik",sans-serif;
  }
  .sign-shapes{position:absolute;inset:0;width:892px;height:1198px;}
  .headline{position:absolute;left:72px;margin:0;font-weight:800;line-height:1;letter-spacing:2px;}
  .headline--for{top:84px;font-size:200px;color:var(--royal);}
  .headline--sale{top:263px;font-size:200px;color:var(--cyan);}
  .call-label{position:absolute;left:0;right:0;top:515px;text-align:center;margin:0;
    font-weight:800;font-size:70px;line-height:1;color:var(--cyan);}
  .phone{position:absolute;left:0;right:0;top:593px;text-align:center;margin:0;
    font-weight:700;font-size:114px;line-height:1;color:var(--navy);letter-spacing:1px;}
  .brand{position:absolute;left:0;right:0;top:960px;text-align:center;margin:0;
    font-weight:400;font-size:66px;line-height:1;color:var(--brand-text);}
</style>
</head>
<body>
<div class="canvas">
  <div class="sign">
    <svg class="sign-shapes" viewBox="0 0 892 1198" aria-hidden="true">
      <!-- top corner bands -->
      <polygon points="0,0 185,0 172,40 0,53" fill="var(--sky)"/>
      <polygon points="185,0 520,0 172,40" fill="var(--ice)"/>
      <polygon points="520,0 892,0 892,57" fill="var(--cyan)"/>
      <!-- divider under headline -->
      <rect x="48" y="462" width="690" height="6" fill="var(--sky)"/>
      <rect x="738" y="462" width="70" height="6" fill="var(--ice)"/>
      <rect x="808" y="462" width="60" height="6" fill="var(--royal)"/>
      <!-- lower brand panel -->
      <rect x="0" y="780" width="892" height="418" fill="var(--mist)"/>
      <rect x="0" y="752" width="892" height="28" fill="var(--sky)"/>
      <rect x="0" y="738" width="892" height="14" fill="var(--royal)"/>
      <!-- rail blocks -->
      <g fill="var(--ice)">
        <rect x="14" y="726" width="44" height="38" rx="6"/>
        <rect x="64" y="730" width="34" height="30" rx="5"/>
        <rect x="104" y="730" width="30" height="30" rx="5"/>
        <rect x="140" y="732" width="18" height="26" rx="4"/>
        <rect x="168" y="738" width="12" height="14" rx="3"/>
        <rect x="712" y="738" width="12" height="14" rx="3"/>
        <rect x="732" y="732" width="18" height="26" rx="4"/>
        <rect x="758" y="730" width="30" height="30" rx="5"/>
        <rect x="794" y="730" width="34" height="30" rx="5"/>
        <rect x="836" y="726" width="44" height="38" rx="6"/>
      </g>
      <!-- bottom corner bands -->
      <polygon points="0,1168 0,1198 190,1198" fill="var(--cyan)"/>
      <polygon points="190,1198 535,1156 525,1198" fill="var(--ice)"/>
      <polygon points="525,1198 540,1157 892,1113 892,1198" fill="var(--sky)"/>
    </svg>

    <h1 class="headline headline--for">FOR</h1>
    <h1 class="headline headline--sale">SALE</h1>
    <p class="call-label">Call me:</p>
    <p class="phone">(555) 617 3489</p>
    <p class="brand">Laurel Creek Homes</p>
  </div>
</div>
</body>
</html>
```